"Maple Hollow" red wine label design

We are a Sydney based company. We need to design a wine label for a Australian red wine.
Front label include following info:
Our brand: "Maple Hollow";
Product name: "Shiraz 2016";
In the bottom with small font: "Wine of Australia", "750ml"
Back label:
the back label would need to be consistent with the front label, with space for one paragraph of tasting notes, and ingredient info etc.
we would like to use white, gold and blue in this label. It should make customer feel the magical and beautiful moment of starry night.

We also need a logo design for the wine brand: "Maple Hollow"

I have attached a few wine bottle that used blue to give you some inspirations.

We need the design in AI file format.

Target Market(s)

both men and women

Industry/Entity Type

It Company

Logo Text

Maple Hollow

Requirements
Nice to have
• gold borderline, words; use of blue and white

```html
<!DOCTYPE html>
<html lang="en">
<head>
<meta charset="utf-8">
<title>Maple Hollow – Shiraz 2016 Label</title>
<link rel="stylesheet" href="https://fonts.googleapis.com/css2?family=Marcellus&family=Josefin+Sans:wght@300;400&display=swap">
<style>
  :root {
    --page: #ededed;
    --navy: #141a4f;
    --navy-deep: #0f1442;
    --navy-soft: #1c2466;
    --gold: #c9a13b;
    --white: #ffffff;
    --ink-soft: #d9dbe8;
  }
  * { box-sizing: border-box; margin: 0; padding: 0; }
  html, body {
    width: 1200px;
    height: 1059px;
    overflow: hidden;
  }
  body {
    background: radial-gradient(ellipse at 50% 45%, #fafafa 0%, var(--page) 70%, #e2e2e2 100%);
    position: relative;
    font-family: "Josefin Sans", sans-serif;
  }

  /* Front label, shown flat */
  .front-label {
    position: absolute;
    left: 165px;
    top: 468px;
    width: 221px;
    height: 408px;
    background: linear-gradient(180deg, var(--navy) 0%, var(--navy-deep) 45%, var(--navy-soft) 75%, #2a2f8a 100%);
    overflow: hidden;
  }
  .front-label .brand-mark {
    position: absolute;
    left: 50%;
    top: 48px;
    transform: translateX(-50%);
  }
  .front-label .brand-name {
    position: absolute;
    top: 100px;
    width: 100%;
    text-align: center;
    font-family: "Marcellus", serif;
    font-size: 21px;
    letter-spacing: 1px;
    color: var(--gold);
    line-height: 24px;
  }
  .front-label .variety {
    position: absolute;
    top: 205px;
    left: 0;
    width: 100%;
    height: 44px;
    border-top: 1px solid var(--gold);
    border-bottom: 1px solid var(--gold);
    text-align: center;
    font-family: "Josefin Sans", sans-serif;
    font-weight: 300;
    font-size: 19px;
    letter-spacing: 2px;
    line-height: 44px;
    color: var(--ink-soft);
  }
  .front-label .skyline {
    position: absolute;
    left: 0;
    top: 285px;
    width: 100%;
    height: 94px;
    background: linear-gradient(180deg, #f4f4f8 0%, var(--white) 100%);
  }
  .front-label .volume {
    position: absolute;
    top: 361px;
    width: 100%;
    text-align: center;
    font-family: "Josefin Sans", sans-serif;
    font-size: 12px;
    letter-spacing: 1px;
    color: #222;
  }
  .front-label .origin-band {
    position: absolute;
    left: 0;
    bottom: 0;
    width: 100%;
    height: 29px;
    background: var(--gold);
    text-align: center;
    font-size: 10px;
    letter-spacing: 2px;
    line-height: 30px;
    color: var(--white);
  }

  /* Brand card */
  .brand-card {
    position: absolute;
    left: 521px;
    top: 400px;
    width: 593px;
    height: 355px;
    background: radial-gradient(ellipse at 50% 40%, var(--navy-soft) 0%, var(--navy) 55%, var(--navy-deep) 100%);
  }
  .brand-card .brand-mark {
    position: absolute;
    left: 50%;
    top: 96px;
    transform: translateX(-50%);
  }
  .brand-card .brand-name {
    position: absolute;
    top: 238px;
    width: 100%;
    text-align: center;
    font-family: "Marcellus", serif;
    font-size: 56px;
    letter-spacing: 3px;
    line-height: 64px;
    color: var(--gold);
  }
</style>
</head>
<body>

  <section class="front-label" aria-label="Front label">
    <svg class="brand-mark" width="18" height="18" viewBox="0 0 18 18" aria-hidden="true">
      <circle cx="9" cy="9" r="7" fill="none" stroke="var(--gold)" stroke-width="1.5"/>
    </svg>
    <h1 class="brand-name">MAPLE HOLLOW</h1>
    <p class="variety">SHIRAZ 2016</p>
    <div class="skyline" role="img" aria-label="White city skyline silhouette"></div>
    <p class="volume">750ml</p>
    <p class="origin-band">WINE OF AUSTRALIA</p>
  </section>

  <section class="brand-card" aria-label="Brand logo">
    <svg class="brand-mark" width="36" height="36" viewBox="0 0 36 36" aria-hidden="true">
      <circle cx="18" cy="18" r="15" fill="none" stroke="var(--gold)" stroke-width="2"/>
    </svg>
    <h2 class="brand-name">MAPLE HOLLOW</h2>
  </section>

</body>
</html>
```